Safety Consultancy focusing on developing exceptional Safety Leaders

I need a full but simple, modern, catchy website to drive business - my focus is on helping organizations to understand the impact that leaders have on safety performance and how they build the processes to make that happen. I already have great branding (logos) built through PixelGuild and can provide all narrative to build out the pages

Target Market(s)

Focused internationally. Typical client has a fairly robust and mature safety culture yet lacks the focused effort to develop all levels of leadership in terms of managing safety. Exercising these competencies results in continued development of an organizations safety culture as well as improved safety performance

Industry/Entity Type

all

Coding

Coded - Design and coding required

Number of Pages Required

4 page

Font styles to use
Other font styles liked:
• to match my branding

Colors
0054AA
0677BA
7BADD7
CADEEF
E8F1F8

Requirements
Must have
• Must utilize my current branding, logo, etc. I want to have a page outlining clearly my vision - which I will add to my uploads as we move forward. I need to have a page listing my extensive and unique experience as well as successes
Nice to have
• Want to leave it up to designers - but needs to be simple and easily navigable - hope to have a resource page that I can update myself with safety resource info, reports, etc.

```html
<!DOCTYPE html>
<html lang="en">
<head>
<meta charset="utf-8">
<title>Halvern Ventures International</title>
<link href="https://fonts.googleapis.com/css2?family=Poppins:wght@400;500;600;700&display=swap" rel="stylesheet">
<style>
:root{
  --blue:#0054AA;
  --blue-mid:#0677BA;
  --blue-soft:#7BADD7;
  --blue-pale:#CADEEF;
  --blue-mist:#E8F1F8;
  --ink:#111318;
  --text:#555a63;
  --white:#ffffff;
}
*{box-sizing:border-box;margin:0;padding:0}
html,body{width:1200px;height:3249px;overflow:hidden}
body{position:relative;font-family:'Poppins',sans-serif;background:var(--white);color:var(--ink)}
.abs{position:absolute}
.brand{display:flex;align-items:center;gap:12px}
.brand-mark{width:30px;height:30px;background:var(--blue)}
.brand-name{font-size:32px;font-weight:600;color:var(--blue);line-height:1}
.nav{top:0;left:0;width:1200px;height:90px}
.nav-links{left:428px;top:38px;display:flex;gap:46px;font-size:12px;color:#333}
.nav-links .active{color:var(--blue);font-weight:500;position:relative}
.nav-links .active::after{content:"";position:absolute;left:50%;top:20px;width:3px;height:3px;border-radius:50%;background:var(--blue)}
.btn{display:inline-flex;align-items:center;justify-content:center;gap:16px;white-space:nowrap;border-radius:10px;font-size:13px;font-weight:500;color:var(--white);background:var(--blue-mid);padding:0 18px;box-shadow:3px 3px 0 var(--blue);text-decoration:none}
.btn svg{width:24px;height:8px;flex:none}
.btn-light{background:var(--blue-mist);color:var(--blue);box-shadow:3px 3px 0 var(--blue-soft)}
.hero-bg{left:0;top:0}
.hero-title{left:141px;top:208px;font-size:44px;font-weight:600;line-height:53px;letter-spacing:.5px}
.accent{color:var(--blue)}
.accent-light{color:var(--blue-soft)}
.hero-sub{left:141px;top:400px;width:460px;font-size:13px;line-height:23px;color:var(--text)}
.section-title{font-size:36px;font-weight:600;line-height:1.2;white-space:nowrap}
.about-text{left:622px;top:890px;width:436px;font-size:13px;line-height:23px;color:var(--text);text-align:justify}
.about-text p+p{margin-top:8px}
.ghost{font-weight:700;color:var(--blue-mist);letter-spacing:6px;white-space:nowrap}
.card-img{width:302px;height:358px;border-radius:24px;clip-path:polygon(0 8%,100% 0,100% 100%,0 100%)}
.card{width:278px;height:186px;background:var(--white);border-radius:22px;box-shadow:0 12px 30px rgba(0,40,90,.12);padding:30px 22px 0}
.card h3{font-size:15px;font-weight:600;color:var(--blue);display:flex;align-items:center;gap:10px;white-space:nowrap}
.card h3 svg{flex:none}
.card p{margin-top:10px;font-size:11px;line-height:20px;color:var(--text);text-align:justify}
.skill{width:260px;text-align:center}
.skill-icon{width:70px;height:70px;border-radius:8px;background:var(--blue);margin:0 auto;display:flex;align-items:center;justify-content:center}
.skill h4{margin-top:18px;font-size:16px;font-weight:600;line-height:24px}
.skill p{margin-top:14px;font-size:12px;line-height:20px;color:var(--text)}
.cta-title{left:0;width:1200px;top:2620px;text-align:center;font-size:42px;font-weight:600;color:var(--white);white-space:nowrap}
.cta-text{left:0;width:1200px;top:2697px;text-align:center;font-size:13px;line-height:24px;color:var(--white)}
.foot-title{font-size:18px;font-weight:600;white-space:nowrap}
.foot-list{list-style:none;font-size:12px;color:var(--text)}
.foot-list li{height:30px;display:flex;align-items:center;gap:10px}
.foot-list li::before{content:"";width:4px;height:4px;border-radius:50%;background:var(--blue)}
.foot-list .active{color:var(--blue);font-weight:500}
.contact-row{display:flex;align-items:center;gap:14px;font-size:12px;color:var(--text);line-height:18px;white-space:nowrap}
.social{width:28px;height:28px;border-radius:50%;background:var(--blue)}
</style>
</head>
<body>

<svg class="abs hero-bg" width="1200" height="800" viewBox="0 0 1200 800">
  <defs>
    <linearGradient id="heroFade" x1="0" y1="0" x2="1" y2="1">
      <stop offset="0" stop-color="#f3f7fb"/>
      <stop offset="1" stop-color="#dbe6f1"/>
    </linearGradient>
  </defs>
  <polygon points="0,0 1200,0 1200,665 0,740" fill="url(#heroFade)"/>
  <line x1="0" y1="778" x2="1200" y2="665" stroke="#0677BA" stroke-width="1" stroke-dasharray="3 3"/>
</svg>

<header class="abs nav">
  <div class="abs brand" style="left:141px;top:30px">
    <span class="brand-mark"></span><span class="brand-name">Halvern</span>
  </div>
  <nav class="abs nav-links">
    <span class="active">Home</span><span>About Us</span><span>Services</span><span>Resources</span>
  </nav>
  <a class="abs btn" style="left:859px;top:28px;height:32px;font-size:11px">Contact Us
    <svg viewBox="0 0 24 8"><path d="M0 4h22M18 1l4 3-4 3" fill="none" stroke="#fff" stroke-width="1.2"/></svg></a>
</header>

<div class="abs" role="img" aria-label="Portrait of the consultant in a blue suit" style="left:680px;top:140px;width:465px;height:528px;background:linear-gradient(160deg,#e6d2c7 0%,#b9c6d8 35%,#1f4fa8 65%,#173e8c 100%);border-radius:200px 200px 0 0"></div>

<h1 class="abs hero-title">Empowering<br>Leadership For Superior<br>Safety <span class="accent">Performance</span></h1>
<svg class="abs" style="left:295px;top:352px" width="296" height="16" viewBox="0 0 296 16"><path d="M2 12 Q150 2 294 10" fill="none" stroke="#0054AA" stroke-width="2"/></svg>
<svg class="abs" style="left:424px;top:182px" width="40" height="60" viewBox="0 0 40 60"><path d="M12 2 L4 20 M16 30 L32 24 M18 50 L38 48" stroke="#0054AA" stroke-width="2" fill="none"/></svg>
<p class="abs hero-sub">Transforming Safety Culture Through Effective Leadership and Process Development.</p>
<a class="abs btn" style="left:141px;top:474px;height:44px">Know More
  <svg viewBox="0 0 24 8"><path d="M0 4h22M18 1l4 3-4 3" fill="none" stroke="#fff" stroke-width="1.2"/></svg></a>

<div class="abs ghost" style="left:1100px;top:712px;font-size:72px;writing-mode:vertical-rl">ABOUT US</div>
<div class="abs" role="img" aria-label="Two women in hard hats reviewing documents" style="left:135px;top:790px;width:430px;height:397px;border-radius:40px 40px 200px 200px;background:linear-gradient(135deg,#e9eef3 0%,#c9d2dc 45%,#c9413c 60%,#d8c1a6 85%)"></div>
<span class="abs" style="left:505px;top:878px;width:60px;height:60px;border-radius:50%;background:#15171c"></span>
<h2 class="abs section-title" style="left:622px;top:830px">Welcome To <span class="accent">Halvern</span></h2>
<div class="abs about-text">
  <p>Lorem ipsum dolor sit amet, consectetur adipiscing elit. Suspendisse feugiat varius molestie. Phasellus cursus ullamcorper nisl congue malesuada.</p>
  <p>Donec molestie ligula eu enim dictum, ut sollicitudin lacus dignissim. Pellentesque cursus arcu nec dui mollis, id hendrerit dui volutpat. In sodales nisl id purus porta, id dictum lacus feugiat. Nulla facilisi.</p>
</div>
<a class="abs btn" style="left:622px;top:1088px;height:44px">Know More
  <svg viewBox="0 0 24 8"><path d="M0 4h22M18 1l4 3-4 3" fill="none" stroke="#fff" stroke-width="1.2"/></svg></a>

<svg class="abs" style="left:0;top:1230px" width="1200" height="640" viewBox="0 0 1200 640">
  <line x1="0" y1="130" x2="1200" y2="6" stroke="#9fb6cc" stroke-width="1"/>
  <polygon points="0,120 1200,45 1200,560 0,635" fill="#0054AA"/>
  <line x1="0" y1="158" x2="1200" y2="80" stroke="#7BADD7" stroke-width="1" opacity=".6"/>
  <line x1="0" y1="140" x2="1200" y2="92" stroke="#7BADD7" stroke-width="1" opacity=".5"/>
</svg>
<div class="abs ghost" style="left:0;width:1200px;top:1395px;text-align:center;font-size:80px;color:rgba(255,255,255,.05)">TESTIMONIALS</div>
<h2 class="abs section-title" style="left:0;width:1200px;top:1436px;text-align:center;color:#fff">What Our <span class="accent-light">Clients Say</span></h2>

<div class="abs card-img" role="img" aria-label="Photo of a smiling man in a grey blazer" style="left:77px;top:1512px;background:linear-gradient(160deg,#c7ccd2,#8c939b)"></div>
<div class="abs card" style="left:128px;top:1732px"><h3><svg width="22" height="16" viewBox="0 0 22 16" fill="#0054AA"><path d="M0 9a7 7 0 0 1 7-9v3a4 4 0 0 0-3 4h3v9H0zM12 9a7 7 0 0 1 7-9v3a4 4 0 0 0-3 4h3v9h-7z"/></svg>Owen Marsh</h3><p>Lorem ipsum dolor sit amet, consectetuer adipiscing elit, sed diam nonummy nibh euismod tincidunt ut laoreet dolore magna aliquam erat volutpat.</p></div>

<div class="abs card-img" role="img" aria-label="Photo of a woman with dark hair outdoors" style="left:435px;top:1512px;background:linear-gradient(160deg,#9b8f80,#3b3430)"></div>
<div class="abs card" style="left:486px;top:1732px"><h3><svg width="22" height="16" viewBox="0 0 22 16" fill="#0054AA"><path d="M0 9a7 7 0 0 1 7-9v3a4 4 0 0 0-3 4h3v9H0zM12 9a7 7 0 0 1 7-9v3a4 4 0 0 0-3 4h3v9h-7z"/></svg>Clara Hollis</h3><p>Lorem ipsum dolor sit amet, consectetuer adipiscing elit, sed diam nonummy nibh euismod tincidunt ut laoreet dolore magna aliquam erat volutpat.</p></div>

<div class="abs card-img" role="img" aria-label="Photo of a young man in a dark coat in a forest" style="left:793px;top:1512px;background:linear-gradient(160deg,#c08a4f,#4a3a2a)"></div>
<div class="abs card" style="left:844px;top:1732px"><h3><svg width="22" height="16" viewBox="0 0 22 16" fill="#0054AA"><path d="M0 9a7 7 0 0 1 7-9v3a4 4 0 0 0-3 4h3v9H0zM12 9a7 7 0 0 1 7-9v3a4 4 0 0 0-3 4h3v9h-7z"/></svg>Leo Fairbank</h3><p>Lorem ipsum dolor sit amet, consectetuer adipiscing elit, sed diam nonummy nibh euismod tincidunt ut laoreet dolore magna aliquam erat volutpat.</p></div>

<svg class="abs" style="left:425px;top:1950px" width="350" height="20" viewBox="0 0 350 20">
  <path d="M2 10h20M8 5L2 10l6 5" fill="none" stroke="#555" stroke-width="1.2"/>
  <path d="M50 10 Q175 6 300 10" fill="none" stroke="#0054AA" stroke-width="2"/>
  <path d="M328 10h20M342 5l6 5-6 5" fill="none" stroke="#0054AA" stroke-width="1.2"/>
</svg>

<div class="abs ghost" style="left:36px;top:1950px;font-size:72px;writing-mode:vertical-rl;transform:rotate(180deg)">SERVICES</div>
<h2 class="abs section-title" style="left:0;width:1200px;top:2058px;text-align:center">Our <span class="accent">Expertise</span></h2>

<div class="abs skill" style="left:155px;top:2145px">
  <div class="skill-icon"><svg width="40" height="40" viewBox="0 0 40 40" fill="none" stroke="#fff" stroke-width="1.5"><circle cx="20" cy="14" r="5"/><path d="M11 32c0-6 4-10 9-10s9 4 9 10z"/><circle cx="8" cy="18" r="3"/><circle cx="32" cy="18" r="3"/></svg></div>
  <h4>Leadership<br>Development</h4><p>Enhancing leadership skills for<br>better safety management.</p>
</div>
<div class="abs skill" style="left:465px;top:2145px">
  <div class="skill-icon"><svg width="40" height="40" viewBox="0 0 40 40" fill="none" stroke="#fff" stroke-width="1.5"><path d="M20 5l12 5v9c0 8-6 13-12 16-6-3-12-8-12-16v-9z"/><path d="M14 20l4 4 8-8"/></svg></div>
  <h4>Safety Culture<br>Improvement</h4><p>Building robust safety processes<br>and culture.</p>
</div>
<div class="abs skill" style="left:776px;top:2145px">
  <div class="skill-icon"><svg width="40" height="40" viewBox="0 0 40 40" fill="none" stroke="#fff" stroke-width="1.5"><circle cx="20" cy="16" r="9"/><path d="M11 16h18M20 7c-4 5-4 13 0 18M20 7c4 5 4 13 0 18"/><rect x="7" y="28" width="26" height="6"/></svg></div>
  <h4>Global<br>Consulting</h4><p>Serving organizations worldwide.</p>
</div>

<svg class="abs" style="left:0;top:2420px" width="1200" height="540" viewBox="0 0 1200 540">
  <polygon points="0,80 1200,8 1200,460 0,530" fill="#0054AA"/>
  <line x1="0" y1="110" x2="1200" y2="32" stroke="#7BADD7" stroke-width="1" opacity=".6"/>
  <line x1="0" y1="124" x2="1200" y2="46" stroke="#7BADD7" stroke-width="1" opacity=".5"/>
</svg>
<div class="abs brand" style="left:585px;top:2562px"><span class="brand-mark" style="background:#fff"></span></div>
<h2 class="abs cta-title">Interested In <span class="accent-light">Our Services?</span></h2>
<svg class="abs" style="left:618px;top:2668px" width="300" height="12" viewBox="0 0 300 12"><path d="M2 8 Q150 0 298 6" fill="none" stroke="#fff" stroke-width="2"/></svg>
<svg class="abs" style="left:905px;top:2598px" width="40" height="60" viewBox="0 0 40 60"><path d="M12 2 L4 20 M16 30 L32 24 M18 50 L38 48" stroke="#fff" stroke-width="2" fill="none"/></svg>
<p class="abs cta-text">Lorem ipsum dolor sit amet, consectetur adipiscing elit. Suspendisse feugiat varius molestie.<br>Phasellus cursus ullamcorper nisl congue malesuada.</p>
<a class="abs btn btn-light" style="left:525px;top:2775px;height:40px">Know More
  <svg viewBox="0 0 24 8"><path d="M0 4h22M18 1l4 3-4 3" fill="none" stroke="#0054AA" stroke-width="1.2"/></svg></a>

<footer>
  <div class="abs brand" style="left:141px;top:3005px"><span class="brand-mark"></span><span class="brand-name">Halvern</span></div>
  <p class="abs" style="left:141px;top:3072px;width:360px;font-size:12px;line-height:18px;color:var(--text)">Transforming Safety Culture Through Effective Leadership and Process Development</p>
  <span class="abs social" style="left:141px;top:3129px"></span>
  <span class="abs social" style="left:180px;top:3129px"></span>

  <h3 class="abs foot-title" style="left:603px;top:2992px">Quick <span class="accent">Links</span></h3>
  <ul class="abs foot-list" style="left:603px;top:3025px">
    <li class="active">Home</li><li>About Us</li><li>Services</li><li>Resources</li><li>Contact Us</li>
  </ul>

  <h3 class="abs foot-title" style="left:832px;top:2992px">Contact <span class="accent">Details</span></h3>
  <div class="abs contact-row" style="left:832px;top:3032px;align-items:flex-start">
    <svg width="12" height="16" viewBox="0 0 12 16" fill="none" stroke="#333" stroke-width="1.2"><path d="M6 15s5-5 5-9A5 5 0 0 0 1 6c0 4 5 9 5 9z"/><circle cx="6" cy="6" r="2"/></svg>
    <span style="font-size:11px">4120 Alder Crescent, Cedar Bay,<br>British Columbia, Canada. V2K 3L9</span>
  </div>
  <div class="abs contact-row" style="left:832px;top:3086px;font-size:14px;font-weight:600;color:var(--blue)">
    <svg width="14" height="14" viewBox="0 0 14 14" fill="none" stroke="#333" stroke-width="1.2"><path d="M3 1l2 3-1.5 1.5a8 8 0 0 0 5 5L10 9l3 2-1 2c-6 0-11-5-11-11z"/></svg>+1-555-014-2781
  </div>
  <div class="abs contact-row" style="left:832px;top:3127px">
    <svg width="14" height="12" viewBox="0 0 14 12" fill="none" stroke="#333" stroke-width="1.2"><rect x="1" y="1" width="12" height="10"/><path d="M1 1l6 5 6-5"/></svg>hello@halvern.example
  </div>

  <div class="abs" style="left:141px;top:3200px;width:918px;height:1px;background:#c9ced6"></div>
  <p class="abs" style="left:0;width:1200px;top:3215px;text-align:center;font-size:11px;color:var(--text)">© 2024 Halvern Ventures International. All Rights Reserved.</p>
</footer>

</body>
</html>
```